Postcard for commercial concrete cleaning company that will be mailed to business customers

A 6x9 postcard that will be mailed out to businesses who have concrete (sidewalks, drive thrus, dumpster pads, etc) that need periodic pressure washing to keep clean. Our current customers are majority restaurants. We are able to remove gum and grease from concrete which is difficult for much of our competitors. We work at night when the businesses are closed or slow if 24hr.

Target Market(s)

This will go to restaurants, banks, gas stations and other retail locations.

Colors

Designer to choose colors to be used in the design.

Requirements
Must have
• Logo. A headline that mentions commercial concrete cleaning so recipients will know at a glance what we do
Nice to have
• The image included is of a fast food doorway that is half cleaned, the right side. Something like "Dirty Doorway?" may make sense.
• We specialize is maintenance concrete cleaning where we come on a regular basis so I like phrase keep your concrete clean, or keep your business clean. something like that.

```html
<!DOCTYPE html>
<html lang="en">
<head>
<meta charset="utf-8">
<title>Commercial Concrete Cleaning Postcard</title>
<link href="https://fonts.googleapis.com/css2?family=Montserrat:wght@800;900&family=Lato:wght@400;700&display=swap" rel="stylesheet">
<style>
  :root {
    --navy: #262f6e;
    --band-blue: #1e6cc0;
    --cyan: #18a8ea;
    --ink: #1c1f3a;
    --white: #ffffff;
    --page: #e9e9ea;
  }
  * { box-sizing: border-box; margin: 0; padding: 0; }
  html, body { width: 1200px; height: 1200px; overflow: hidden; }
  body { background: var(--page); font-family: "Lato", sans-serif; color: var(--ink); position: relative; }

  .postcard { position: absolute; left: 210px; width: 780px; height: 520px; background: var(--white); box-shadow: 0 6px 16px rgba(0,0,0,.25); overflow: hidden; }
  .postcard--front { top: 50px; }
  .postcard--back { top: 630px; }

  /* Front */
  .hero-photo { position: absolute; left: 0; top: 0; width: 780px; height: 332px;
    background: linear-gradient(180deg, #8f8a84 0%, #d9dcdf 30%, #9b8c7c 45%, #a9a394 60%, #b9ad92 100%); }
  .headline-band { position: absolute; left: 0; top: 332px; width: 780px; height: 66px; background: var(--band-blue);
    display: flex; align-items: center; padding-left: 26px; }
  .headline { font-family: "Montserrat", sans-serif; font-weight: 900; color: var(--white); font-size: 35px; letter-spacing: .5px; }
  .brand { position: absolute; left: 28px; top: 428px; }
  .brand-name { font-family: "Montserrat", sans-serif; font-weight: 800; color: var(--navy); font-size: 27px; line-height: 1; }
  .brand-tag { font-family: "Lato", sans-serif; color: var(--navy); font-size: 21px; letter-spacing: 5.4px; margin-top: 6px; }
  .contact-list { position: absolute; left: 415px; top: 422px; list-style: none; }
  .contact-list li { display: flex; align-items: center; gap: 10px; font-size: 22px; line-height: 29px; color: var(--ink); }
  .contact-list svg { width: 20px; height: 20px; fill: var(--ink); flex: none; }

  /* Back */
  .about-panel { position: absolute; left: 0; top: 0; width: 390px; height: 298px; background: var(--navy); color: var(--white); padding: 26px 30px 0 32px; }
  .section-title { font-size: 14px; font-weight: 700; margin-bottom: 12px; }
  .about-panel p { font-size: 8.6px; line-height: 11.6px; margin-bottom: 10px; }
  .services { position: absolute; left: 32px; top: 316px; width: 340px; }
  .services .section-title { color: var(--ink); margin-bottom: 10px; }
  .services ul { list-style: none; }
  .services li { font-size: 8px; line-height: 26.5px; padding-left: 20px; position: relative; }
  .services li::before { content: ""; position: absolute; left: 0; top: 10px; width: 8px; height: 8px; border-radius: 50%; background: var(--cyan); }
  .contact-bar { position: absolute; left: 0; bottom: 0; width: 390px; height: 44px; background: var(--cyan); display: flex; align-items: center; justify-content: space-evenly; font-size: 8px; color: var(--ink); }
  .contact-bar span { display: flex; align-items: center; gap: 6px; }
  .contact-bar svg { width: 9px; height: 9px; fill: var(--ink); }
  .mail-side { position: absolute; left: 390px; top: 0; width: 390px; height: 520px; }
  .mail-brand { position: absolute; left: 18px; top: 22px; }
  .mail-brand .name { font-family: "Montserrat", sans-serif; font-weight: 800; color: var(--navy); font-size: 10px; }
  .mail-brand .tag { font-size: 7px; letter-spacing: 2px; color: var(--navy); }
  .stamp-box { position: absolute; right: 35px; top: 24px; width: 88px; height: 100px; border: 1.5px solid var(--ink); }
  .address-line { position: absolute; left: 15px; width: 340px; height: 1px; background: #9a9aa0; }
</style>
</head>
<body>

<section class="postcard postcard--front">
  <div class="hero-photo" role="img" aria-label="Photo of a storefront doorway with glass doors, stone walls and a black trash can; the concrete walkway is half pressure washed, the right half visibly cleaner"></div>
  <div class="headline-band"><h1 class="headline">COMMERCIAL CONCRETE CLEANING</h1></div>
  <div class="brand">
    <div class="brand-name">Riverbend Commercial</div>
    <div class="brand-tag">PRESSURE WASHING</div>
  </div>
  <ul class="contact-list">
    <li><svg viewBox="0 0 24 24"><path d="M6.6 10.8a15 15 0 0 0 6.6 6.6l2.2-2.2c.3-.3.7-.4 1-.2 1.1.4 2.3.6 3.6.6.6 0 1 .4 1 1V20c0 .6-.4 1-1 1A17 17 0 0 1 3 4c0-.6.4-1 1-1h3.5c.6 0 1 .4 1 1 0 1.3.2 2.5.6 3.6.1.3 0 .7-.2 1z"/></svg>+1 555 014 2280</li>
    <li><svg viewBox="0 0 24 24"><path d="M2 5h20v14H2zm2 2v.5l8 5.5 8-5.5V7zm0 3v7h16v-7l-8 5.5z"/></svg>hello@riverbendwash.com</li>
    <li><svg viewBox="0 0 24 24"><circle cx="12" cy="12" r="10"/></svg>www.riverbendwash.com</li>
  </ul>
</section>

<section class="postcard postcard--back">
  <div class="about-panel">
    <h2 class="section-title">About Us</h2>
    <p>Lorem ipsum dolor sit amet, consectetur adipiscing elit. Nam quis nunc tristique, sagittis elit eu, pretium magna. Nam faucibus volutpat lacus nec molestie. Sed ante ante, mattis vitae erat ac, mollis fermentum odio. Integer dolor risus, posuere sed viverra et, finibus in turpis. Sed nec elit aliquet, blandit lectus in, dapibus ex. In eget dolor iaculis, sodales nunc vitae, elementum est.</p>
    <p>Lorem ipsum dolor sit amet, consectetur adipiscing elit. Nam quis nunc tristique, sagittis elit eu, pretium magna. Nam faucibus volutpat lacus nec molestie. Sed ante ante, mattis vitae erat ac, mollis fermentum odio. Integer dolor risus, posuere sed viverra et, finibus in turpis. Sed nec elit aliquet, blandit lectus in, dapibus ex. In eget dolor iaculis, sodales nunc vitae, elementum est.</p>
    <p>Lorem ipsum dolor sit amet, consectetur adipiscing elit. Nam quis nunc tristique, sagittis elit eu, pretium magna. Nam faucibus volutpat lacus nec molestie. Sed ante ante, mattis vitae erat ac, mollis fermentum odio. Integer dolor risus, posuere sed viverra et, finibus in turpis. Sed nec elit aliquet, blandit lectus in, dapibus ex. In eget dolor iaculis, sodales nunc vitae, elementum est.</p>
  </div>
  <div class="services">
    <h2 class="section-title">Services</h2>
    <ul>
      <li>Neque porro quisquam est qui dolorem ipsum quia dolor sit amet, consectetur</li>
      <li>Neque porro quisquam est qui dolorem ipsum quia dolor sit amet, consectetur</li>
      <li>Neque porro quisquam est qui dolorem ipsum quia dolor sit amet, consectetur</li>
      <li>Neque porro quisquam est qui dolorem ipsum quia dolor sit amet, consectetur</li>
      <li>Neque porro quisquam est qui dolorem ipsum quia dolor sit amet, consectetur</li>
    </ul>
  </div>
  <div class="contact-bar">
    <span><svg viewBox="0 0 24 24"><path d="M6.6 10.8a15 15 0 0 0 6.6 6.6l2.2-2.2c.3-.3.7-.4 1-.2 1.1.4 2.3.6 3.6.6.6 0 1 .4 1 1V20c0 .6-.4 1-1 1A17 17 0 0 1 3 4c0-.6.4-1 1-1h3.5c.6 0 1 .4 1 1 0 1.3.2 2.5.6 3.6.1.3 0 .7-.2 1z"/></svg>+1 555 014 2280</span>
    <span><svg viewBox="0 0 24 24"><circle cx="12" cy="12" r="10"/></svg>www.riverbendwash.com</span>
    <span><svg viewBox="0 0 24 24"><path d="M2 5h20v14H2zm2 2v.5l8 5.5 8-5.5V7zm0 3v7h16v-7l-8 5.5z"/></svg>hello@riverbendwash.com</span>
  </div>
  <div class="mail-side">
    <div class="mail-brand">
      <div class="name">Riverbend Commercial</div>
      <div class="tag">PRESSURE WASHING</div>
    </div>
    <div class="stamp-box"></div>
    <div class="address-line" style="top:225px"></div>
    <div class="address-line" style="top:258px"></div>
    <div class="address-line" style="top:291px"></div>
    <div class="address-line" style="top:325px"></div>
    <div class="address-line" style="top:364px"></div>
  </div>
</section>

</body>
</html>
```